Themed design for packaging sleeve and box

1) Gable box 330w x 200d x 160h (image attached for illustration purposes)
2) Sleeve to wrap around our food trays - see image attached

See the images uploaded!!!
This should not be copied, as some are from our competitors and are subject to Copywrite but gives an idea what kind of packaging we would be creating

From all the designs submitted, we will choose one final design and work with this designer to create our full packaging range.....

Target Market(s)

Working adults and health mined people

Font styles to use
Sans Serif

Colors

Designer to choose colors to be used in the design.

Requirements
Must have
• A clean modern look, striking design
Same design in different colours (see the drink bottles idea)
1) meat in shades of red
2) fish in shades of blue
3) vegetable in shades of green
Nice to have
• abstract white against strong colours
use shapes or mosaic or shades of the same colours
Should not have
• overpacked designs with too much information

```html
<!DOCTYPE html>
<html lang="en">
<head>
<meta charset="utf-8">
<title>Evenleaf Kosher Meals – Organic Veggies Sleeve</title>
<link rel="stylesheet" href="https://fonts.googleapis.com/css2?family=Montserrat:wght@700&family=Josefin+Sans:wght@300&display=swap">
<style>
  :root {
    --backdrop: #cccccc;
    --veg-green: #8cc540;
    --veg-green-soft: #93c948;
    --veg-line: #6e9a2f;
    --white: #ffffff;
  }
  html, body {
    margin: 0;
    padding: 0;
    width: 1200px;
    height: 1000px;
    overflow: hidden;
    background: var(--backdrop);
  }
  .canvas {
    position: relative;
    width: 1200px;
    height: 1000px;
    background: var(--backdrop);
  }
  .sleeve {
    position: absolute;
    left: 115px;
    top: 131px;
    width: 977px;
    height: 738px;
    overflow: hidden;
    background: var(--veg-green);
  }
  .veg-pattern {
    position: absolute;
    inset: 0;
    background: radial-gradient(ellipse at 50% 70%, var(--veg-green-soft), var(--veg-green) 70%);
  }
  .brand-arc {
    position: absolute;
    left: 123px;
    top: -362px;
    width: 730px;
    height: 704px;
    border-radius: 50%;
    background: var(--white);
  }
  .brand-name {
    position: absolute;
    left: 0;
    right: 0;
    top: 62px;
    margin: 0;
    text-align: center;
    font-family: "Montserrat", sans-serif;
    font-weight: 700;
    font-size: 86px;
    letter-spacing: 6px;
    line-height: 1;
    color: var(--veg-green);
  }
  .brand-tagline {
    position: absolute;
    left: 0;
    right: 0;
    top: 184px;
    margin: 0;
    text-align: center;
    font-family: "Josefin Sans", sans-serif;
    font-weight: 300;
    font-size: 40px;
    letter-spacing: 22px;
    line-height: 1;
    color: var(--veg-green);
  }
  .range-label {
    position: absolute;
    left: 78px;
    top: 514px;
    width: 826px;
    height: 97px;
    box-sizing: border-box;
    border: 3px solid var(--veg-line);
    border-radius: 12px;
    display: flex;
    align-items: center;
    justify-content: center;
    font-family: "Montserrat", sans-serif;
    font-weight: 700;
    font-size: 66px;
    letter-spacing: 4px;
    color: var(--white);
  }
</style>
</head>
<body>
  <main class="canvas">
    <section class="sleeve">
      <div class="veg-pattern" role="img" aria-label="Scattered line drawings of vegetables: cabbage, peppers, pumpkin, garlic, tomato, corn, potato, peas and broccoli"></div>
      <div class="brand-arc"></div>
      <h1 class="brand-name">EVENLEAF</h1>
      <p class="brand-tagline">KOSHER MEALS</p>
      <div class="range-label">ORGANIC VEGGIES</div>
    </section>
  </main>
</body>
</html>
```